integrative health clinic-Medical massage, acupuncture, chiropractic

we like our logo, but are open to new ideas. We need a new card design. We have added chiropractic and acupuncture that we have put under the name of the business. We are an integrative medical clinic

Target Market(s)

General public, athletes

Contact Information for Business Card

Phone 5055583927
Fax 5055583926
Hours Monday-Friday 9-6
Saturday 10-6
The 20% can be smaller on the back

Colors
3176b5
0355a3

Requirements
Must have
• Logo but am open to ideas
Nice to have
• We are an integrated medical clinic but also want to be personable. We want the card fun and inviting

```html
<!DOCTYPE html>
<html lang="en">
<head>
<meta charset="utf-8">
<title>Full Circle Wellness – Business Card</title>
<link rel="stylesheet" href="https://fonts.googleapis.com/css2?family=Oswald:wght@400&family=Roboto:ital,wght@0,400;0,500;0,700;1,500;1,700&family=Libre+Baskerville:ital@1&display=swap">
<style>
  :root {
    --brand-blue: #2b3e9c;
    --card-white: #f9f9f9;
    --ink: #111111;
    --backdrop: #e9e6e1;
  }
  * { box-sizing: border-box; margin: 0; padding: 0; }
  html, body { width: 900px; height: 1200px; overflow: hidden; }
  body {
    background: var(--backdrop);
    position: relative;
    font-family: "Roboto", Arial, sans-serif;
    color: var(--ink);
  }
  .card {
    position: absolute;
    left: 75px;
    width: 768px;
    background: var(--card-white);
    border-radius: 18px;
    overflow: hidden;
  }
  .card--front { top: 133px; height: 438px; }
  .card--back { top: 627px; height: 441px; }
  .card__band { position: absolute; inset: 0; }
  .abs { position: absolute; }
  .centered { text-align: center; transform: translateX(-50%); white-space: nowrap; }

  /* Front */
  .brand-name {
    left: 85px; top: 44px;
    font-family: "Oswald", "Arial Narrow", sans-serif;
    font-size: 43px; line-height: 1; color: var(--ink);
    letter-spacing: -0.3px;
  }
  .brand-mark {
    left: 112px; top: 98px; width: 44px; height: 44px;
    border-radius: 50%; background: var(--brand-blue);
  }
  .brand-tagline {
    left: 178px; top: 100px;
    font-family: "Libre Baskerville", Georgia, serif;
    font-style: italic; font-size: 17px; color: var(--ink);
  }
  .specialties {
    left: 283px; top: 188px;
    font-style: italic; font-weight: 500; font-size: 21px; line-height: 25px;
    letter-spacing: 0.3px;
  }
  .social-dot {
    left: 265px; top: 289px; width: 36px; height: 36px;
    border-radius: 50%; background: var(--brand-blue);
  }
  .contact {
    left: 283px; top: 345px;
    font-size: 19px; line-height: 27px;
  }

  /* Back */
  .offer { left: 348px; top: 38px; width: 270px; height: 36px; }
  .offer__text {
    position: absolute; left: 39px; top: 2px; width: 192px; height: 30px;
    background: var(--brand-blue); color: #fff;
    font-style: italic; font-weight: 700; font-size: 18px; line-height: 30px;
    text-align: center;
  }
  .book {
    left: 483px; top: 94px;
    font-style: italic; font-weight: 700; font-size: 27px; line-height: 32px;
  }
  .website {
    left: 483px; top: 127px;
    font-style: italic; font-weight: 500; font-size: 19px;
  }
  .hours {
    left: 483px; top: 183px;
    font-size: 21px; line-height: 27px; font-weight: 500;
  }
  .hours strong { font-weight: 700; }
  .pin { left: 463px; top: 250px; width: 40px; height: 40px; }
  .address { left: 483px; top: 299px; font-size: 19px; }
  .insurance {
    left: 483px; top: 360px;
    font-style: italic; font-weight: 500; font-size: 17px; line-height: 24px;
  }
  .back-mark {
    left: 52px; top: 306px; width: 104px; height: 104px;
    border-radius: 50%; background: var(--card-white);
  }
</style>
</head>
<body>

<section class="card card--front" aria-label="Card front">
  <svg class="card__band" width="768" height="438" viewBox="0 0 768 438" role="img" aria-label="Blue band with a dotted pattern">
    <path d="M513 0 Q656 219 515 438 L768 438 L768 0 Z" fill="var(--brand-blue)"/>
  </svg>
  <h1 class="abs brand-name">Full Circle Wellness</h1>
  <div class="abs brand-mark" aria-hidden="true"></div>
  <p class="abs brand-tagline">Sports Therapy and Wellness Center</p>
  <p class="abs centered specialties">Specialzing in<br>Medcal, Chiropractic &amp; Acupuncture,<br>Sports Massage &amp; Manual Therapies</p>
  <div class="abs social-dot" aria-hidden="true"></div>
  <p class="abs centered contact">P: (505) 558 - 3927 &nbsp;|&nbsp; F: (505) 558 3926<br>E: Info@fullcirclewellnessnm.com</p>
</section>

<section class="card card--back" aria-label="Card back">
  <svg class="card__band" width="768" height="441" viewBox="0 0 768 441" role="img" aria-label="Blue band with a dotted pattern">
    <path d="M0 0 L255 0 Q95 220 255 441 L0 441 Z" fill="var(--brand-blue)"/>
  </svg>
  <div class="abs back-mark" aria-hidden="true"></div>

  <div class="abs offer">
    <svg width="270" height="36" viewBox="0 0 270 36" aria-hidden="true">
      <path d="M0 8 L46 8 L46 34 L0 34 L12 21 Z" fill="var(--brand-blue)"/>
      <path d="M270 8 L224 8 L224 34 L270 34 L258 21 Z" fill="var(--brand-blue)"/>
    </svg>
    <div class="offer__text">20% Off First Visit</div>
  </div>

  <p class="abs centered book">BOOK ONLINE</p>
  <p class="abs centered website">www.fullcirclewellnessnm.com</p>
  <p class="abs centered hours"><strong>Hours Monday - Friday</strong> 9:00am - 6:00pm<br><strong>Saturday</strong> 10:00am -6:00pm</p>

  <svg class="abs pin" viewBox="0 0 40 40" aria-label="Location">
    <circle cx="20" cy="20" r="20" fill="var(--brand-blue)"/>
    <path d="M20 9 C14.5 9 11 13 11 17.5 C11 23 20 31 20 31 C20 31 29 23 29 17.5 C29 13 25.5 9 20 9 Z" fill="#fff"/>
    <circle cx="20" cy="17.5" r="3.5" fill="var(--brand-blue)"/>
  </svg>
  <p class="abs centered address">418 Juniper Ave, B4, Santa Fe, Nm 87505</p>
  <p class="abs centered insurance">We Accept some insurances,<br>Worker’s Comp &amp; Personal Injury</p>
</section>

</body>
</html>
```